Halvo KT Biz Card Design

Residential / Commercial/ Emergency

Industry/Entity Type

Residential

Contact Information for Business Card

Tomas Welker
President
PO Box 4827
Corvell Bay, NY 11080
tomas@halvo-kt.com
631.555.0172
855.HALVO.KT
www.halvo-kt.com
FB: Halvo KT
Twitter: HALVO KT

```html
<!DOCTYPE html>
<html lang="en">
<head>
<meta charset="utf-8">
<title>Halvo KT Business Card</title>
<link href="https://fonts.googleapis.com/css2?family=Oswald:wght@400;500;600;700&display=swap" rel="stylesheet">
<style>
  :root {
    --amber: #e9a321;
    --amber-band: #e6a526;
    --charcoal: #2f3538;
    --paper: #f7f7f5;
    --white: #ffffff;
    --stage: #e4e2de;
    --rule: #8a9094;
  }
  * { box-sizing: border-box; margin: 0; padding: 0; }
  html, body { width: 1200px; height: 885px; overflow: hidden; }
  body {
    background: var(--stage);
    font-family: "Oswald", "Arial Narrow", sans-serif;
    position: relative;
  }
  .card {
    position: absolute;
    left: 250px;
    width: 700px;
    height: 400px;
    background: var(--paper);
    overflow: hidden;
    box-shadow: 0 6px 18px rgba(0,0,0,.18);
  }
  .card--front { top: 28px; }
  .card--back { top: 457px; }

  .company-name {
    position: absolute;
    left: 40px;
    top: 30px;
    font-family: "Oswald", "Arial Narrow", sans-serif;
    font-weight: 500;
    font-size: 84px;
    line-height: 1.2;
    color: var(--amber);
    white-space: nowrap;
  }

  /* front */
  .front-band {
    position: absolute;
    left: 0; top: 168px;
    width: 100%; height: 172px;
    background: var(--charcoal);
  }
  .identity {
    position: absolute;
    left: 40px; top: 18px;
    width: 270px;
  }
  .identity__name {
    font-weight: 700;
    font-size: 34px;
    line-height: 1.1;
    color: var(--white);
  }
  .identity__title {
    font-weight: 700;
    font-size: 28px;
    line-height: 1.1;
    color: var(--amber);
    margin-bottom: 6px;
  }
  .social {
    display: flex;
    align-items: center;
    gap: 10px;
    font-weight: 700;
    font-size: 20px;
    line-height: 1.3;
    color: var(--white);
  }
  .social__mark {
    width: 18px; height: 18px;
    background: var(--amber);
    display: inline-block;
  }
  .band-divider {
    position: absolute;
    left: 330px; top: 22px;
    width: 2px; height: 128px;
    background: var(--rule);
  }
  .contacts {
    position: absolute;
    left: 360px; top: 18px;
  }
  .contacts__hotline {
    font-weight: 700;
    font-size: 24px;
    color: var(--amber);
    line-height: 1.3;
    margin-bottom: 4px;
  }
  .contact {
    display: flex;
    align-items: center;
    gap: 12px;
    font-weight: 600;
    font-size: 22px;
    line-height: 1.45;
    color: var(--white);
  }
  .contact__icon {
    width: 22px; height: 22px;
    background: var(--amber);
    border-radius: 3px;
    display: flex; align-items: center; justify-content: center;
  }
  .contact__icon svg { width: 14px; height: 14px; }
  .front-address {
    position: absolute;
    left: 40px; top: 348px;
    font-weight: 700;
    font-size: 26px;
    color: var(--amber);
  }

  /* back */
  .back-band {
    position: absolute;
    left: 0; top: 170px;
    width: 100%; height: 172px;
    background: var(--amber-band);
  }
  .service-list {
    position: absolute;
    top: 20px;
    list-style: none;
    font-weight: 500;
    font-size: 22px;
    line-height: 1.25;
    color: var(--white);
  }
  .service-list--east { left: 40px; }
  .service-list--north { left: 370px; }
  .back-divider {
    position: absolute;
    left: 340px; top: 24px;
    width: 2px; height: 124px;
    background: var(--charcoal);
  }
  .back-footer {
    position: absolute;
    left: 0; top: 342px;
    width: 100%; height: 58px;
    background: var(--charcoal);
  }
  .back-address {
    position: absolute;
    left: 40px; top: 8px;
    font-weight: 700;
    font-size: 26px;
    color: var(--amber);
  }
</style>
</head>
<body>

<section class="card card--front">
  <div class="company-name">Halvo KT</div>
  <div class="front-band">
    <div class="identity">
      <div class="identity__name">Tomas Welker</div>
      <div class="identity__title">President</div>
      <div class="social"><span>HALVO KT</span><span class="social__mark"></span></div>
      <div class="social"><span>Halvo KT</span><span class="social__mark"></span></div>
    </div>
    <div class="band-divider"></div>
    <div class="contacts">
      <div class="contacts__hotline">855.HALVO.KT</div>
      <div class="contact">
        <span class="contact__icon"><svg viewBox="0 0 16 16"><path d="M3 1.5l3 .5 1 3.5-2 1.2a9 9 0 0 0 4.3 4.3l1.2-2 3.5 1 .5 3c-.3.7-1 1-1.8 1A12.5 12.5 0 0 1 1 3.3c0-.8.3-1.5 2-1.8z" fill="#fff"/></svg></span>
        <span>631.555.0172</span>
      </div>
      <div class="contact">
        <span class="contact__icon"><svg viewBox="0 0 16 16"><rect x="1" y="3" width="14" height="10" fill="none" stroke="#fff" stroke-width="1.6"/><path d="M1 3l7 6 7-6" fill="none" stroke="#fff" stroke-width="1.6"/></svg></span>
        <span>tomas@halvo-kt.com</span>
      </div>
      <div class="contact">
        <span class="contact__icon"><svg viewBox="0 0 16 16"><circle cx="8" cy="8" r="6.5" fill="none" stroke="#fff" stroke-width="1.5"/><ellipse cx="8" cy="8" rx="2.8" ry="6.5" fill="none" stroke="#fff" stroke-width="1.3"/><path d="M1.5 8h13" stroke="#fff" stroke-width="1.3"/></svg></span>
        <span>www.halvo-kt.com</span>
      </div>
    </div>
  </div>
  <div class="front-address">PO Box 4827&nbsp;&nbsp;Corvell Bay, NY 11080</div>
</section>

<section class="card card--back">
  <div class="company-name">Halvo KT</div>
  <div class="back-band">
    <ul class="service-list service-list--east">
      <li>East End Skyview</li>
      <li>Hampton Skyview</li>
      <li>Long Island Skyview</li>
      <li>Drone Services</li>
      <li>Nassau Skyview</li>
    </ul>
    <div class="back-divider"></div>
    <ul class="service-list service-list--north">
      <li>North Fork Skyview</li>
      <li>NY Skyview</li>
      <li>NYC Skyview</li>
      <li>Suffolk Skyview</li>
    </ul>
  </div>
  <div class="back-footer">
    <div class="back-address">PO Box 4827&nbsp;&nbsp;Corvell Bay, NY 11080</div>
  </div>
</section>

</body>
</html>
```